Stationary for a Consulting Firm
The Summit Compass Incorporated
Project: Stationary for a Consulting Firm
Stationary for a Consulting Firm - Consulting
Creative Brief
Professional
Dr. Gordon T. Feld
President
47 Maple Crest Okotoks, AB T2Q 4M9
gfeld@summitcompass.ca
www.summitcompass.ca
Business Cards, Stationary, Fax Cover Sheet, and Envelopes are required
Canada's Summit Compass

```html
<!DOCTYPE html>
<html lang="en">
<head>
<meta charset="utf-8">
<title>The Summit Compass Incorporated – Business Card</title>
<link href="https://fonts.googleapis.com/css2?family=Open+Sans:ital,wght@0,400;0,600;0,800;1,400&display=swap" rel="stylesheet">
<style>
  :root {
    --page-bg: #f1f3f5;
    --brand-blue: #2f9fd8;
    --brand-blue-deep: #1b86c3;
    --brand-blue-light: #7cc6ec;
    --stripe-pale: #cfeaf8;
    --card-white: #ffffff;
    --text-white: #ffffff;
    --card-shadow: rgba(20, 50, 80, 0.22);
  }
  * { box-sizing: border-box; margin: 0; padding: 0; }
  html, body {
    width: 1200px;
    height: 1009px;
    overflow: hidden;
    background: var(--page-bg);
    font-family: "Open Sans", Arial, sans-serif;
  }
  .stage { position: relative; width: 1200px; height: 1009px; }

  .card {
    position: absolute;
    width: 540px;
    height: 310px;
    border-radius: 18px;
    overflow: hidden;
    box-shadow: 0 14px 30px var(--card-shadow);
  }
  .card-back { left: 620px; top: 190px; background: linear-gradient(160deg, var(--brand-blue) 0%, var(--brand-blue-deep) 100%); }
  .card-front { left: 60px; top: 500px; background: var(--card-white); }

  .card-art { position: absolute; inset: 0; width: 100%; height: 100%; }

  .back-website {
    position: absolute;
    left: 30px; top: 28px;
    color: var(--text-white);
    font-size: 12px;
    font-style: italic;
    letter-spacing: 2.5px;
  }
  .back-mark {
    position: absolute;
    right: 36px; bottom: 36px;
    width: 92px; height: 92px;
    border-radius: 50%;
    background: rgba(255, 255, 255, 0.14);
  }

  .contact-list {
    position: absolute;
    left: 22px; top: 118px;
    list-style: none;
    color: var(--text-white);
    font-size: 10.5px;
    line-height: 1.35;
  }
  .contact-list li { display: flex; align-items: flex-start; gap: 8px; margin-bottom: 5px; }
  .contact-icon { flex: none; width: 13px; height: 13px; margin-top: 1px; }

  .brand {
    position: absolute;
    left: 268px; top: 92px;
    display: flex;
    align-items: center;
    gap: 12px;
  }
  .brand-dot {
    width: 46px; height: 46px;
    border-radius: 50%;
    background: var(--brand-blue);
    flex: none;
  }
  .brand-name {
    color: var(--brand-blue);
    font-weight: 800;
    font-size: 25px;
    line-height: 1.02;
    letter-spacing: 0.5px;
    text-transform: uppercase;
  }

  .holder {
    position: absolute;
    right: 24px; bottom: 16px;
    text-align: right;
    color: var(--text-white);
  }
  .holder-name { font-size: 12.5px; font-weight: 600; }
  .holder-title { font-size: 10.5px; }
</style>
</head>
<body>
<main class="stage">

  <section class="card card-back" aria-label="Business card, back">
    <p class="back-website">www.summitcompass.ca</p>
    <div class="back-mark"></div>
  </section>

  <section class="card card-front" aria-label="Business card, front">
    <svg class="card-art" viewBox="0 0 540 310" preserveAspectRatio="none" aria-hidden="true">
      <defs>
        <linearGradient id="frontBlue" x1="0" y1="0" x2="1" y2="1">
          <stop offset="0" stop-color="#36a6dd"/>
          <stop offset="1" stop-color="#1b86c3"/>
        </linearGradient>
      </defs>
      <rect width="540" height="310" fill="url(#frontBlue)"/>
      <path d="M150 0 C185 150 330 236 540 250 V310 H540 V272 C315 262 168 170 128 0 Z" fill="var(--brand-blue-light)" opacity="0.55"/>
      <path d="M165 0 C198 140 340 222 540 234 V250 C330 236 185 150 150 0 Z" fill="var(--stripe-pale)"/>
      <path d="M180 0 H540 V222 C350 212 212 132 180 0 Z" fill="var(--card-white)"/>
    </svg>

    <ul class="contact-list">
      <li>
        <svg class="contact-icon" viewBox="0 0 16 16"><circle cx="8" cy="8" r="8" fill="#fff"/><path d="M8 3.5a3 3 0 0 0-3 3c0 2.2 3 5.8 3 5.8s3-3.6 3-5.8a3 3 0 0 0-3-3zm0 4.2a1.2 1.2 0 1 1 0-2.4 1.2 1.2 0 0 1 0 2.4z" fill="#1b86c3"/></svg>
        <span>47 Maple Crest<br>Okotoks, AB T2Q 4M9</span>
      </li>
      <li>
        <svg class="contact-icon" viewBox="0 0 16 16"><circle cx="8" cy="8" r="8" fill="#fff"/><path d="M5.2 4h1.6l.8 2-1 .8a5 5 0 0 0 2.6 2.6l.8-1 2 .8v1.6c0 .5-.4.8-.9.8A7 7 0 0 1 4.4 4.9c0-.5.3-.9.8-.9z" fill="#1b86c3"/></svg>
        <span>(403) 555-0142</span>
      </li>
      <li>
        <svg class="contact-icon" viewBox="0 0 16 16"><circle cx="8" cy="8" r="8" fill="#fff"/><rect x="5" y="3.5" width="6" height="9" rx="1" fill="#1b86c3"/><rect x="6" y="4.8" width="4" height="5.5" fill="#fff"/></svg>
        <span>(403) 555-0178</span>
      </li>
      <li>
        <svg class="contact-icon" viewBox="0 0 16 16"><circle cx="8" cy="8" r="8" fill="#fff"/><rect x="4" y="5" width="8" height="6" rx="0.8" fill="#1b86c3"/><path d="M4.3 5.4 8 8.4l3.7-3" stroke="#fff" stroke-width="0.9" fill="none"/></svg>
        <span>gfeld@summitcompass.ca</span>
      </li>
      <li>
        <svg class="contact-icon" viewBox="0 0 16 16"><circle cx="8" cy="8" r="8" fill="#fff"/><circle cx="8" cy="8" r="4" fill="none" stroke="#1b86c3" stroke-width="1"/><path d="M4 8h8M8 4c-2 2.4-2 5.6 0 8M8 4c2 2.4 2 5.6 0 8" stroke="#1b86c3" stroke-width="0.8" fill="none"/></svg>
        <span>www.summitcompass.ca</span>
      </li>
    </ul>

    <div class="brand">
      <span class="brand-dot"></span>
      <p class="brand-name">Summit<br>Compass</p>
    </div>

    <div class="holder">
      <p class="holder-name">Dr. Gordon T. Feld</p>
      <p class="holder-title">President</p>
    </div>
  </section>

</main>
</body>
</html>
```